Financial Services Company Needs New UI/UX

Hello!

We would like to see some UI/UX ideas for our software platform. I've attached a screen capture of our current "dashboard" (or main home page, essentially). We're looking for a very simple, clean, sleek design as there are many different pages throughout the system that will all need to coordinate. You can also view our website to see the colors and general "look" we have on there. It would be ideal for the portal to coordinate with the website since that is how they access the login page. Please submit your best ideas for the dashboard and we will reach out to our favorite designer to move forward with the rest of the pages. You can find our color hex codes on our website on the "Media" page. Should you need any other supporting logos or files please send us a message and we will try to accommodate.

Thanks!

Website: www.ledgerharbor-example.com

Target Market(s)

Our clients are contractors in the construction industry and our software helps them manage material purchases for their jobs.

Industry/Entity Type

Financial Service

Font styles to use
Sans Serif

Requirements
Must have
• The same content and language as the current dashboard but an updated look.
Should not have
• Too much distraction or busy patterns, we're looking for clean and simple and user friendly. Likely a solid or subtly textured background would be best.

```html
<!DOCTYPE html>
<html lang="en">
<head>
<meta charset="utf-8">
<title>LedgerHarbor Dashboard</title>
<link rel="stylesheet" href="https://fonts.googleapis.com/css2?family=Roboto:wght@300;400;500;700&display=swap">
<style>
:root{
  --backdrop:#6b7380;
  --topbar:#2b2e33;
  --logo-bg:#24272b;
  --navbar:#1f2226;
  --nav-text:#c9cdd2;
  --accent-blue:#3d86cc;
  --orange:#e0561c;
  --panel-bg:#eef2f6;
  --white:#ffffff;
  --ink:#222629;
  --muted:#3c4247;
  --line:#e3e7eb;
  --table-head:#d3dee7;
  --col-head:#b0712f;
  --green:#2fb24a;
  --info:#b27a45;
  --dark-dot:#2b2e33;
}
*{box-sizing:border-box;margin:0;padding:0}
html,body{width:1200px;height:743px;overflow:hidden}
body{background:var(--backdrop);font-family:"Roboto",sans-serif;color:var(--ink);position:relative}
.app{position:absolute;left:68px;top:48px;width:1064px;height:648px;background:var(--white);overflow:hidden}
.topbar{position:absolute;left:0;top:0;width:100%;height:66px;background:var(--topbar);color:#8d949b;font-size:11.5px}
.brand{position:absolute;left:0;top:0;width:194px;height:66px;background:var(--logo-bg);display:flex;align-items:center;padding-left:26px;gap:8px;color:#fff;font-size:13px;font-weight:400}
.brand-dot{width:22px;height:22px;border-radius:50%;background:var(--accent-blue)}
.contact{position:absolute;top:0;height:66px;display:flex;align-items:center;gap:8px}
.contact.phone{left:228px}
.contact.mail{left:427px}
.divider{position:absolute;left:400px;top:22px;width:1px;height:22px;background:#4a4f55}
.user{position:absolute;right:34px;top:0;height:66px;display:flex;align-items:center;gap:8px;font-size:12.5px;color:#a6acb2}
.avatar{width:22px;height:22px;border-radius:50%;background:#7a8087;display:flex;align-items:flex-end;justify-content:center;overflow:hidden}
.caret{margin-right:14px}
.navbar{position:absolute;left:0;top:66px;width:100%;height:36px;background:var(--navbar)}
.nav-item{position:absolute;top:0;height:36px;display:flex;align-items:center;gap:8px;color:var(--nav-text);font-size:11.5px;letter-spacing:.2px}
.nav-item.active{background:#2b2f34;color:var(--accent-blue);padding:0 30px}
.nav-item.active::after{content:"";position:absolute;left:50%;bottom:0;margin-left:-6px;border:6px solid transparent;border-bottom-color:var(--panel-bg)}
.overview{position:absolute;left:0;top:102px;width:100%;height:294px;background:var(--panel-bg)}
.page-head{position:absolute;left:132px;top:11px;width:800px;height:45px;background:var(--white);border:1px solid var(--line);display:flex;align-items:center;padding-left:16px;gap:9px}
.page-head h1{font-size:20px;font-weight:300;color:var(--ink)}
.help{width:16px;height:16px;border-radius:50%;background:var(--accent-blue);color:#fff;font-size:10px;font-weight:700;display:flex;align-items:center;justify-content:center}
.toggle{position:absolute;right:14px;top:11px;width:22px;height:22px;background:var(--orange);display:flex;align-items:center;justify-content:center}
.card{position:absolute;top:80px;width:254px;height:182px;background:var(--white);text-align:center}
.card .badge{position:absolute;left:50%;top:-9px;margin-left:-9px;width:18px;height:18px;border-radius:50%;background:var(--dark-dot);color:#fff;font-size:10px;font-weight:700;display:flex;align-items:center;justify-content:center}
.card .badge.action{background:var(--green)}
.card h2{font-size:12.5px;font-weight:500;height:42px;line-height:50px;border-bottom:1px solid var(--line)}
.card .amount{font-size:27px;font-weight:700;color:var(--accent-blue);margin-top:14px}
.card .meta{font-size:8.5px;color:var(--muted);line-height:13.5px;margin-top:14px}
.card .meta.single{margin-top:20px}
.actions{position:absolute;left:0;right:0;bottom:17px;display:flex;justify-content:center;gap:4px}
.btn{background:var(--orange);color:#fff;font-size:9.5px;height:22px;line-height:22px;border-radius:2px;padding:0 0;text-align:center}
.legend{position:absolute;left:0;width:100%;top:275px;display:flex;justify-content:center;gap:24px;font-size:8.5px;color:var(--muted)}
.legend span{display:flex;align-items:center;gap:5px}
.dot{width:11px;height:11px;border-radius:50%;color:#fff;font-size:7px;font-weight:700;display:inline-flex;align-items:center;justify-content:center}
.dot.action{background:var(--green)}
.dot.info{background:var(--info)}
.panel{position:absolute;top:406px;height:222px;border:1px solid var(--line);background:var(--white)}
.panel.tasks{left:132px;width:392px}
.panel.jobs{left:540px;width:392px}
.panel-head{height:31px;background:var(--table-head);display:flex;align-items:center;gap:7px;padding-left:10px;font-size:13px;font-weight:500}
table{width:100%;border-collapse:collapse;table-layout:fixed;font-size:8.5px;color:var(--muted)}
th{font-weight:400;color:var(--col-head);font-size:9.5px;text-align:left;height:32px;padding-left:10px;border-right:1px solid var(--line);border-bottom:1px solid var(--line)}
td{height:32px;padding-left:10px;border-right:1px solid var(--line);border-bottom:1px solid var(--line);line-height:11px}
tr:nth-child(even) td{background:#f6f7f9}
th:last-child,td:last-child{border-right:none}
.num{text-align:right;padding-right:10px;padding-left:0}
th.num{text-align:left;padding-left:12px}
.info-cell{padding-left:7px}
.info-cell .dot{width:17px;height:17px;font-size:10px}
</style>
</head>
<body>
<div class="app">
  <header class="topbar">
    <div class="brand"><span class="brand-dot"></span>LedgerHarbor</div>
    <div class="contact phone">
      <svg width="14" height="14" viewBox="0 0 14 14"><circle cx="7" cy="7" r="6.3" fill="none" stroke="#6d747b"/><path d="M5 4.2l1 1.4-.6.8c.4.9 1.1 1.6 2 2l.8-.6 1.4 1-.6 1.1c-2.2-.3-4.2-2.3-4.6-4.6z" fill="#6d747b"/></svg>
      Support: 555-014-2290
    </div>
    <div class="divider"></div>
    <div class="contact mail">
      <svg width="14" height="10" viewBox="0 0 14 10"><rect x=".5" y=".5" width="13" height="9" fill="none" stroke="#6d747b"/><path d="M.5.5L7 5.5 13.5.5" fill="none" stroke="#6d747b"/></svg>
      help@northgatesupply-example.com
    </div>
    <div class="user">
      <svg class="caret" width="11" height="7" viewBox="0 0 11 7"><path d="M0 0h11L5.5 7z" fill="var(--orange)"/></svg>
      <span class="avatar"><svg width="16" height="18" viewBox="0 0 16 18"><circle cx="8" cy="7" r="3.5" fill="#2b2e33"/><path d="M1 18c0-4 3-6.5 7-6.5s7 2.5 7 6.5z" fill="#2b2e33"/></svg></span>
      user101@sample-mail.com
    </div>
  </header>

  <nav class="navbar">
    <div class="nav-item active" style="left:132px;width:152px">
      <svg width="16" height="14" viewBox="0 0 16 14"><path d="M2 12a6.5 6.5 0 1 1 12 0" fill="none" stroke="var(--accent-blue)" stroke-width="1.3"/><path d="M8 9l3-4" stroke="var(--accent-blue)" stroke-width="1.3"/></svg>
      DASHBOARD
    </div>
    <div class="nav-item" style="left:306px">
      <svg width="16" height="16" viewBox="0 0 16 16" fill="none" stroke="#c9cdd2" stroke-width="1.2"><path d="M2 14l8-8M10 2l4 4-2 2-4-4zM3 2l3 3-1 1-3-3zM9 10l4 4"/></svg>
      JOB CENTER
    </div>
    <div class="nav-item" style="left:457px">
      <svg width="17" height="12" viewBox="0 0 17 12" fill="none" stroke="#c9cdd2" stroke-width="1.2"><rect x=".6" y=".6" width="15.8" height="10.8"/><path d="M.6 4h15.8M3 8h5"/></svg>
      PAYMENTS
    </div>
    <div class="nav-item" style="left:599px">
      <svg width="16" height="16" viewBox="0 0 16 16" fill="none" stroke="#c9cdd2" stroke-width="1.2"><path d="M1 5L8 1l7 4zM3 6v7M6.3 6v7M9.7 6v7M13 6v7M1 14.5h14"/></svg>
      CREDIT MANAGEMENT
    </div>
    <div class="nav-item" style="left:790px">
      <svg width="13" height="16" viewBox="0 0 13 16" fill="none" stroke="#c9cdd2" stroke-width="1.2"><path d="M.6.6h8l3.8 3.8v11H.6zM3 7h7M3 10h7M3 13h7"/></svg>
      PRELIEN CENTER
    </div>
  </nav>

  <section class="overview">
    <div class="page-head">
      <span class="help">?</span>
      <h1>Dashboard</h1>
      <div class="toggle"><svg width="10" height="6" viewBox="0 0 10 6"><path d="M0 0h10L5 6z" fill="#fff"/></svg></div>
    </div>

    <div class="card" style="left:132px">
      <span class="badge">i</span>
      <h2>AVAILABLE MASTER CREDIT</h2>
      <p class="amount">$129,500.00</p>
      <p class="meta single">Master Credit Limit: $250,000.00</p>
      <div class="actions"><span class="btn" style="width:117px">Setup New Job</span></div>
    </div>
    <div class="card" style="left:406px">
      <span class="badge">i</span>
      <h2>LAST PAYMENT</h2>
      <p class="amount">$500.00</p>
      <p class="meta single">Last Payment Date: 6/28/2016</p>
      <div class="actions"><span class="btn" style="width:106px">Veiw Payments</span><span class="btn" style="width:106px">Veiw Billings</span></div>
    </div>
    <div class="card" style="left:678px">
      <span class="badge action">!</span>
      <h2>NEXT PAYMENT</h2>
      <p class="amount">$158.95</p>
      <p class="meta">Due Date: 7/11/2016<br>Current Principal: $9,968.46<br>Minimum Interest/Fees: $158.95</p>
      <div class="actions"><span class="btn" style="width:117px">Make Payment</span></div>
    </div>

    <div class="legend">
      <span><i class="dot action">!</i>Indicates an action is required</span>
      <span><i class="dot info">?</i>Information only - no action required</span>
    </div>
  </section>

  <section class="panel tasks">
    <div class="panel-head">
      <svg width="14" height="16" viewBox="0 0 14 16" fill="none" stroke="#222629" stroke-width="1.3"><rect x=".7" y="2" width="12.6" height="13.3"/><path d="M4.5.7h5v2.6h-5zM3.5 7h7M3.5 10h7M3.5 13h5"/></svg>
      Task Summary
    </div>
    <table>
      <colgroup><col style="width:33px"><col style="width:134px"><col style="width:134px"><col></colgroup>
      <tr><th></th><th>Task</th><th>Status</th><th>Received</th></tr>
      <tr><td class="info-cell"><i class="dot info">?</i></td><td>Supplier Invoice</td><td>Confirmation by Account Manager Pending</td><td>5/01/2016</td></tr>
      <tr><td></td><td></td><td></td><td></td></tr>
      <tr><td></td><td></td><td></td><td></td></tr>
      <tr><td></td><td></td><td></td><td></td></tr>
      <tr><td></td><td></td><td></td><td></td></tr>
    </table>
  </section>

  <section class="panel jobs">
    <div class="panel-head">
      <svg width="14" height="16" viewBox="0 0 14 16" fill="none" stroke="#222629" stroke-width="1.3"><rect x=".7" y="2" width="12.6" height="13.3"/><path d="M4.5.7h5v2.6h-5zM4 9.5l2 2 4-4.5"/></svg>
      Active Jobs
    </div>
    <table>
      <colgroup><col style="width:77px"><col style="width:84px"><col style="width:67px"><col style="width:89px"><col></colgroup>
      <tr><th>Job#</th><th>Job Name</th><th>Status</th><th class="num">Credit Limit</th><th>Avail. Credit</th></tr>
      <tr><td>pc101-001</td><td>Job-001</td><td>Active</td><td class="num">$50,100.00</td><td class="num">$35,100.00</td></tr>
      <tr><td>pc101-002</td><td>Job-002</td><td>Active</td><td class="num">$40,000.00</td><td class="num">$2000.00</td></tr>
      <tr><td>pc101-003</td><td>Job-003</td><td>Active</td><td class="num">$22,000.00</td><td class="num">$0.00</td></tr>
      <tr><td>pc101-004</td><td>Job-004</td><td>Active</td><td class="num">$10,400.00</td><td class="num">$10,400.00</td></tr>
      <tr><td></td><td></td><td></td><td></td><td></td></tr>
    </table>
  </section>
</div>
</body>
</html>
```